Conveyancing Brochure

I am after a 4 page brochure for our Conveyancing division in our law firm Brantford Wylie Osgood Lawyers.

We are a diverse range of energetic, dynamic and innovative professionals who strive to be at the forefront of progressive legal service. Please refer to our website for more information: www.bwolegal.com.au

I would like to see the colours of our logo & also some images incorporated throughout the brochure (however I don't want it to look 'too busy' either).

The images can be based around the range of services that we provide eg: residential, development etc.

Thank you,
Maris

```html
<!DOCTYPE html>
<html lang="en">
<head>
<meta charset="utf-8">
<title>Brantford Wylie Osgood Lawyers – Conveyancing Brochure</title>
<link rel="stylesheet" href="https://fonts.googleapis.com/css2?family=Roboto:wght@300;400&display=swap">
<style>
  :root {
    --paper: #ffffff;
    --ink: #1d1d1f;
    --band-light: #2a93c4;
    --band-dark: #1b6389;
    --accent-blue: #1f6d95;
    --soft-grey: #9a9a9a;
    --fold: #3a88b4;
    --text-white: #ffffff;
  }
  * { margin: 0; padding: 0; box-sizing: border-box; }
  html, body { width: 1200px; height: 423px; overflow: hidden; background: var(--paper); }
  .spread {
    position: relative; width: 1200px; height: 423px; overflow: hidden;
    font-family: "Roboto", Arial, sans-serif; color: var(--ink); background: var(--paper);
  }
  .fold-line {
    position: absolute; left: 599px; top: 0; width: 1px; height: 423px; background: var(--fold); z-index: 2;
  }
  .feature-band {
    position: absolute; left: 0; top: 156px; width: 1200px; height: 104px;
    background: linear-gradient(90deg, var(--band-light) 0%, var(--band-dark) 50%, var(--band-dark) 52%, var(--band-light) 100%);
  }
  .page { position: absolute; top: 0; width: 600px; height: 423px; }
  .page--back { left: 0; }
  .page--front { left: 600px; }

  .wordmark { position: absolute; display: flex; align-items: center; font-weight: 300; color: var(--ink); }
  .wordmark__name { line-height: 0.95; letter-spacing: -0.02em; }
  .wordmark__sub { display: block; text-align: right; letter-spacing: 0.02em; }
  .wordmark__dot { border-radius: 50%; background: var(--accent-blue); flex: none; }

  .wordmark--small { left: 46px; top: 36px; font-size: 15px; }
  .wordmark--small .wordmark__sub { font-size: 8px; margin-top: 2px; }
  .wordmark--small .wordmark__dot { width: 14px; height: 14px; margin-left: 10px; }

  .wordmark--large { left: 188px; top: 36px; font-size: 33px; }
  .wordmark--large .wordmark__sub { font-size: 15px; margin-top: 4px; }
  .wordmark--large .wordmark__dot { width: 28px; height: 28px; margin-left: 18px; }

  .band-message {
    position: absolute; left: 0; top: 172px; width: 600px; text-align: center;
    color: var(--text-white); font-size: 17.5px; line-height: 23px; font-weight: 400;
  }
  .contact-note {
    position: absolute; left: 0; top: 364px; width: 600px; text-align: center;
    font-size: 10px; line-height: 13px; color: var(--ink);
  }

  .tagline {
    position: absolute; left: 172px; top: 164px; width: 264px; height: 90px;
    color: var(--text-white); text-align: center; font-weight: 300;
  }
  .tagline::before, .tagline::after {
    content: ""; position: absolute; top: 0; width: 8px; height: 90px;
    border: 3px solid var(--text-white);
  }
  .tagline::before { left: 0; border-right: none; }
  .tagline::after { right: 0; border-left: none; }
  .tagline__line { display: block; font-size: 19px; line-height: 28px; }
  .tagline__line:first-child { margin-top: 3px; }
  .tagline__big { font-size: 24px; }

  .values { position: absolute; left: 0; top: 0; width: 600px; height: 423px; font-weight: 300; }
  .value { position: absolute; white-space: nowrap; line-height: 1; }
  .value--major { color: var(--soft-grey); font-size: 48px; }
  .value--minor { color: var(--accent-blue); font-size: 29px; }
  .value--approachability { left: 148px; top: 270px; }
  .value--accountability { left: 92px; top: 322px; }
  .value--availability { left: 354px; top: 322px; }
  .value--accessibility { left: 152px; top: 352px; }
</style>
</head>
<body>
<main class="spread">
  <div class="feature-band"></div>
  <div class="fold-line"></div>

  <section class="page page--back">
    <div class="wordmark wordmark--small">
      <div class="wordmark__name">Brantford<br>Wylie Osgood<span class="wordmark__sub">LAWYERS</span></div>
      <span class="wordmark__dot"></span>
    </div>
    <p class="band-message">Consider using one of our experienced lawyers<br>and not a conveyancer to handle the legal work<br>associated with your transaction.</p>
    <p class="contact-note">For advice on conveyancing or a quote, please contact us on 1300 555 018<br>or email enquiries@bwolegal.com.au</p>
  </section>

  <section class="page page--front">
    <div class="wordmark wordmark--large">
      <div class="wordmark__name">Brantford<br>Wylie Osgood<span class="wordmark__sub">LAWYERS</span></div>
      <span class="wordmark__dot"></span>
    </div>
    <div class="tagline">
      <span class="tagline__line">a <span class="tagline__big">new age</span> firm with a</span>
      <span class="tagline__line"><span class="tagline__big">unique outlook</span> on</span>
      <span class="tagline__line"><span class="tagline__big">practising law</span></span>
    </div>
    <div class="values">
      <span class="value value--major value--approachability">+ approachability</span>
      <span class="value value--minor value--accountability">+ accountability</span>
      <span class="value value--minor value--availability">+ availability</span>
      <span class="value value--major value--accessibility">+ accessibility</span>
    </div>
  </section>
</main>
</body>
</html>
```